Boutique Real Estate Brokerage looking for business card, letterhead and envelope design

We are looking for a cohesive design for our business cards, letterhead and envelopes and that mirrors our high-end homes and clientele. Cedar & Vane is being launched and designed for the marketplace of tomorrow. We grew from the #1 team in our community into a full-service firm that is going to revolutionize the traditional real estate model.

We understand that it’s more important than ever to help our clients and partners adapt to behavioral and market changes being driven by generational shifts and technological advances in society, and by combining traditional brokerage services with innovative production and marketing capabilities, we know how to do that better than anyone else.

Requirements
Must have
• business card, letterhead and envelope design - attached logo.

```html
<!DOCTYPE html>
<html lang="en">
<head>
<meta charset="utf-8">
<title>Cedar &amp; Vane — Business Card</title>
<link rel="stylesheet" href="https://fonts.googleapis.com/css2?family=Montserrat:wght@600;700&family=Arimo:wght@400;700&display=swap">
<style>
  :root {
    --backdrop: #2b2422;
    --card: #0b0b0c;
    --violet-deep: #221878;
    --violet-mid: #3a2fa6;
    --violet-light: #6a5fc8;
    --gold: #c98a3e;
    --ink-light: #d9d9dc;
    --rule: #4a4a4e;
  }
  * { box-sizing: border-box; margin: 0; padding: 0; }
  html, body { width: 1200px; height: 842px; overflow: hidden; }
  body {
    background: var(--backdrop);
    position: relative;
    font-family: "Arimo", Arial, sans-serif;
  }
  .card {
    position: absolute;
    top: 266px;
    width: 540px;
    height: 310px;
    background: var(--card);
    overflow: hidden;
    box-shadow: 0 18px 40px rgba(0,0,0,.55);
  }
  .card--contact { left: 45px; }
  .card--brand { left: 615px; }

  .band {
    position: absolute;
    left: 0; right: 0;
    height: 14px;
    background: linear-gradient(90deg, var(--violet-deep) 0%, var(--violet-light) 50%, var(--violet-deep) 100%);
  }
  .band--top { top: 0; }
  .band--bottom { bottom: 0; }

  .contact {
    position: absolute;
    left: 0; right: 0;
    top: 46px;
    text-align: center;
    color: var(--ink-light);
  }
  .contact__name {
    font-family: "Montserrat", Arial, sans-serif;
    font-weight: 700;
    font-size: 22px;
    letter-spacing: .5px;
    color: var(--gold);
    line-height: 1.1;
  }
  .contact__role { font-size: 13.5px; margin-top: 2px; }
  .rule {
    width: 170px;
    height: 1px;
    background: var(--rule);
    margin: 10px auto;
  }
  .contact__line { font-size: 14px; line-height: 1.42; }
  .contact__label { color: var(--gold); font-weight: 700; }
  .contact__web { color: var(--gold); }
  .contact__address { font-size: 14px; line-height: 1.4; }

  .tab {
    position: absolute;
    width: 46px;
    height: 68px;
    background: linear-gradient(180deg, var(--violet-light), var(--violet-mid) 55%, var(--violet-deep));
  }
  .tab--left { left: 0; top: 150px; border-right: 4px solid var(--gold); }
  .tab--right { right: 0; top: 42px; border-left: 4px solid var(--gold); }

  .brand {
    position: absolute;
    left: 0; right: 0;
    top: 130px;
    display: flex;
    align-items: center;
    justify-content: center;
    gap: 14px;
  }
  .brand__square { width: 36px; height: 36px; background: var(--gold); }
  .brand__name {
    font-family: "Montserrat", Arial, sans-serif;
    font-weight: 700;
    font-size: 30px;
    letter-spacing: 1px;
    color: var(--violet-mid);
    text-transform: uppercase;
  }
</style>
</head>
<body>
  <section class="card card--contact">
    <div class="band band--top"></div>
    <div class="contact">
      <p class="contact__name">DANIEL MERCER</p>
      <p class="contact__role">Managing Director</p>
      <div class="rule"></div>
      <p class="contact__line"><span class="contact__label">P:</span> 044-555 010 240</p>
      <p class="contact__line"><span class="contact__label">M:</span> 044-555 010 240</p>
      <p class="contact__line"><span class="contact__label">E:</span> hello@cedarvane.co</p>
      <p class="contact__line contact__web">www.cedarvane.co</p>
      <div class="rule"></div>
      <p class="contact__address">12345, Address Goes Here<br>Country Name, 123456</p>
    </div>
    <div class="band band--bottom"></div>
  </section>

  <section class="card card--brand">
    <div class="tab tab--left"></div>
    <div class="tab tab--right"></div>
    <div class="brand">
      <span class="brand__square"></span>
      <span class="brand__name">Cedar &amp; Vane</span>
    </div>
  </section>
</body>
</html>
```